Web Design Project for a new download application :-)

We need a website design and a logo design for a new website and desktop application.
The Website will be www.Fetchora.com
The installed application will be: Fetchora

Fetchora is a desktop application that searches and finds all kind of Media files (Movies, Games, Songs, software, etc..)
Fetchora will also manage the download process for the selected files.
Fetchora automates the whole search and download process.

User Flow:
users will initially visit the website.
user will download the application from the website
user will install the application on his computer.
user will run and use the application.

What makes our software special:
-Great search engine for searching media files.
-Very high speed downloads. maximum speeds.
-Allow used to Search by: file type, size, date, format
-Pause and resume downloads
-Get any file you want instantly.
-Unlimited Downloads.

We will need:
Logo
WebSite Design
Icons for the desktop application.

we need only PSDs - no codded pages are needed !

Design to the following screen Size & resolution: 1024 x 768

Target Market(s)

movies and music lovers.
users who download movies, games, softwares, music etc...

Industry/Entity Type

Software

Requirements
Must have
• must have download button

Files

```html
<!DOCTYPE html>
<html lang="en">
<head>
<meta charset="utf-8">
<title>Fetchora — Search, Download, Play</title>
<link rel="stylesheet" href="https://fonts.googleapis.com/css2?family=Nunito:wght@700;800;900&family=Source+Sans+3:wght@400;600&display=swap">
<style>
:root{
  --slate:#3c5873;
  --sky:#19a9ef;
  --sky-light:#5fd0ff;
  --sky-deep:#0f8fd8;
  --ink-blue:#1f5f92;
  --orange:#ff8a00;
  --orange-dark:#e06a00;
  --text:#2e2e2e;
  --heading:#4a4a4a;
  --footer:#1a8fd5;
  --footer-dark:#1d68a6;
  --footer-link:#1e6fb0;
  --white:#ffffff;
}
*{margin:0;padding:0;box-sizing:border-box}
html,body{width:1200px;height:1147px;overflow:hidden;background:var(--white)}
.page{position:relative;width:1200px;height:1147px;font-family:"Source Sans 3",sans-serif;color:var(--text)}
.header{position:absolute;left:0;top:0;width:1200px;height:86px;background:var(--slate)}
.hero{position:absolute;left:0;top:86px;width:1200px;height:401px;
  background:radial-gradient(ellipse 600px 300px at 560px 260px,#8fe3ff 0%,var(--sky-light) 35%,var(--sky) 75%,var(--sky-deep) 100%)}
.hero-tab{position:absolute;left:0;top:58px;width:460px;height:30px;background:#2fb6f5;border-top-right-radius:16px}
.logo{position:absolute;left:179px;top:8px;font-family:"Nunito",sans-serif;font-weight:800;font-size:40px;color:var(--orange);letter-spacing:-0.5px}
.nav{position:absolute;top:28px;left:0;font-family:"Nunito",sans-serif;font-weight:800;font-size:20px}
.nav a{position:absolute;top:0;color:var(--orange);text-decoration:none;white-space:nowrap;line-height:34px}
.nav .active{left:480px;width:77px;height:34px;background:var(--orange);color:var(--white);border-radius:8px;text-align:center}
.nav .active::after{content:"";position:absolute;left:34px;top:33px;border:5px solid transparent;border-top:8px solid var(--orange)}
.flags{position:absolute;top:36px;left:926px;display:flex;gap:12px}
.flags svg{display:block}
.hero-title{position:absolute;left:166px;top:190px;font-family:"Nunito",sans-serif;font-weight:900;color:var(--ink-blue);text-shadow:0 1px 0 rgba(255,255,255,.45)}
.hero-title h1{font-size:45px;line-height:48px;letter-spacing:-1px}
.hero-title p{font-size:26px;line-height:29px;font-weight:800;letter-spacing:-.3px}
.cta{position:absolute;left:210px;top:330px;width:233px;height:81px;border-radius:41px;
  background:linear-gradient(#ffb13b,var(--orange) 55%,var(--orange-dark));box-shadow:0 8px 14px rgba(0,60,110,.35);
  font-family:"Nunito",sans-serif;font-weight:900;color:var(--ink-blue);text-decoration:none}
.cta span{position:absolute;left:28px;top:15px;font-size:24px;line-height:25px}
.cta span small{font-size:21px}
.cta svg{position:absolute;right:18px;top:25px}
.app-shot{position:absolute;left:665px;top:150px;width:336px;height:228px;border:3px solid #1c4f86;
  background:linear-gradient(#1e5d9a 0 22px,#eef3f8 22px 100%);box-shadow:0 12px 22px rgba(0,60,110,.3)}
.features{position:absolute;top:535px;left:0;width:1200px}
.feature{position:absolute;top:0}
.feature svg{position:absolute;left:0;top:0}
.feature h2{position:absolute;top:0;font-weight:600;font-size:19px;color:var(--heading);white-space:nowrap}
.feature p{position:absolute;top:34px;width:190px;font-size:13px;line-height:16px}
.divider{position:absolute;left:175px;top:722px;width:820px;height:8px;border-radius:50%;
  background:radial-gradient(ellipse at center,rgba(0,0,0,.18),rgba(0,0,0,0) 70%)}
.why h2{position:absolute;left:191px;top:786px;font-family:"Nunito",sans-serif;font-weight:800;font-size:31px;color:var(--orange)}
.why p{position:absolute;left:191px;top:846px;width:448px;font-size:13px;line-height:16.8px}
.app-mark{position:absolute;left:760px;top:784px;width:170px;height:160px}
.app-mark .tile{position:absolute;left:20px;top:0;width:147px;height:150px;border-radius:18px;
  background:linear-gradient(#5fd0ff,var(--sky-deep));box-shadow:-40px 10px 0 -10px rgba(95,208,255,.3)}
.app-mark .name{position:absolute;left:20px;top:118px;width:147px;text-align:center;font-family:"Nunito",sans-serif;font-weight:800;font-size:26px;color:var(--white)}
.footer{position:absolute;left:0;top:1030px;width:1200px;height:117px;background:linear-gradient(var(--sky-deep),var(--footer))}
.footer-nav a{position:absolute;top:44px;font-family:"Nunito",sans-serif;font-weight:800;font-size:14px;color:var(--footer-link);text-decoration:none}
.social-title{position:absolute;left:856px;top:15px;font-family:"Nunito",sans-serif;font-weight:800;font-size:13px;color:var(--footer-link)}
.social{position:absolute;left:850px;top:36px;display:flex;gap:7px}
.social span{display:block;width:35px;height:35px;border-radius:50%;background:var(--footer-dark);position:relative}
.social svg{position:absolute;left:9px;top:11px}
.copyright{position:absolute;left:174px;top:94px;font-size:11px;color:var(--footer-link)}
</style>
</head>
<body>
<div class="page">
  <header class="header">
    <div class="logo">Fetchora</div>
    <nav class="nav">
      <a class="active" href="#">Home</a>
      <a href="#" style="left:584px">Download</a>
      <a href="#" style="left:707px">Support</a>
      <a href="#" style="left:807px">Affiliates</a>
    </nav>
    <div class="flags">
      <svg width="20" height="13" aria-label="English"><rect width="20" height="13" fill="#fff"/><rect y="0" width="20" height="2" fill="#c8102e"/><rect y="4" width="20" height="2" fill="#c8102e"/><rect y="8" width="20" height="2" fill="#c8102e"/><rect y="12" width="20" height="1" fill="#c8102e"/><rect width="9" height="7" fill="#2a3d8f"/></svg>
      <svg width="20" height="13" aria-label="French"><rect width="7" height="13" fill="#1f3fa0"/><rect x="7" width="6" height="13" fill="#fff"/><rect x="13" width="7" height="13" fill="#e22030"/></svg>
      <svg width="20" height="13" aria-label="Russian"><rect width="20" height="4.3" fill="#fff"/><rect y="4.3" width="20" height="4.4" fill="#1f3fa0"/><rect y="8.7" width="20" height="4.3" fill="#e22030"/></svg>
    </div>
  </header>
  <div class="hero-tab"></div>
  <section class="hero">
    <div class="hero-title" style="top:104px">
      <h1>Get it talk about it.</h1>
      <p>Search, Download, Play Music.</p>
      <p>Download videos, games and more!</p>
    </div>
    <a class="cta" href="#" style="top:244px">
      <span>DOWNLOAD<br>NOW <small>Fetchora</small></span>
      <svg width="30" height="30" viewBox="0 0 30 30"><circle cx="15" cy="15" r="14" fill="#ffb13b" stroke="#c85c00" stroke-width="2"/><path d="M15 7v12M9.5 14l5.5 6 5.5-6" fill="none" stroke="#c85c00" stroke-width="3.5" stroke-linecap="round"/></svg>
    </a>
    <div class="app-shot" style="top:64px" role="img" aria-label="Screenshot of the Fetchora desktop player showing the music library with album covers and a now-playing list"></div>
  </section>

  <section class="features">
    <div class="feature" style="left:191px">
      <svg width="52" height="58" viewBox="0 0 52 58"><rect width="52" height="58" rx="8" fill="#1997d8"/><rect x="11" y="7" width="30" height="14" rx="2" fill="#0b5f9a"/><circle cx="26" cy="38" r="11" fill="none" stroke="#0b5f9a" stroke-width="4"/></svg>
      <h2 style="left:77px">Store your stuff</h2>
      <p style="left:75px">Lorem ipsum dolor sit amet, con-sectetuer adipiscing elit. Aenean com commodo ligula eget dolor. Aenean massa. Cum sociis natoque penatibus et magnis dis parturient montes, nascetur ridiculus mus.</p>
    </div>
    <div class="feature" style="left:468px">
      <svg width="52" height="58" viewBox="0 0 52 58"><rect width="52" height="58" rx="8" fill="#1997d8"/><path d="M11 36V28a15 15 0 0 1 30 0v8" fill="none" stroke="#0b5f9a" stroke-width="4"/><rect x="7" y="32" width="8" height="13" rx="3" fill="#0b5f9a"/><rect x="37" y="32" width="8" height="13" rx="3" fill="#0b5f9a"/></svg>
      <h2 style="left:81px">Listen &amp; Enjoy!</h2>
      <p style="left:81px;width:184px">Lorem ipsum dolor sit amet, con-sectetuer adipiscing elit. Aenean com commodo ligula eget dolor. Aenean massa. Cum sociis natoque penatibus et magnis dis parturient montes, nascetur ridiculus mus.</p>
    </div>
    <div class="feature" style="left:755px">
      <svg width="52" height="58" viewBox="0 0 52 58"><rect width="52" height="58" rx="8" fill="#1997d8"/><rect x="7" y="16" width="38" height="28" rx="3" fill="#0b5f9a"/><rect x="15" y="20" width="22" height="20" fill="#3cb2ec"/></svg>
      <h2 style="left:71px">Upload and publish!</h2>
      <p style="left:74px;width:190px">Lorem ipsum dolor sit amet, con-sectetuer adipiscing elit. Aenean com commodo ligula eget dolor. Aenean massa. Cum sociis natoque penatibus et magnis dis parturient montes, nascetur ridiculus mus.</p>
    </div>
  </section>

  <div class="divider"></div>

  <section class="why">
    <h2>Why Fetchora is the best?</h2>
    <p>Lorem ipsum dolor sit amet, consectetuer adipiscing elit. Aenean commodo ligula eget dolor. Aenean massa. Cum sociis natoque penatibus et magnis dis parturient montes, nascetur ridiculus mus. Donec quam felis, ultricies nec, pellentesque eu, pretium quis, sem. Nulla consequat massa quis enim. Donec pede justo, fringilla vel, aliquet nec, vulputate eget, arcu. In enim justo, rhoncus ut, imperdiet a, venenatis vitae, justo. Nullam dictum felis eu pede mollis pretium. Integer tincidunt. Cras dapibus. Vivamus elementum semper nisi. Aenean vulputate eleifend tellus.</p>
    <div class="app-mark" aria-label="Fetchora application icon">
      <div class="tile"></div>
      <div class="name">Fetchora</div>
    </div>
  </section>

  <footer class="footer">
    <nav class="footer-nav">
      <a href="#" style="left:461px">Home</a>
      <a href="#" style="left:527px">Download</a>
      <a href="#" style="left:623px">Support</a>
      <a href="#" style="left:702px">Affiliates</a>
    </nav>
    <div class="social-title">GET TO KNOW US...</div>
    <div class="social">
      <span aria-label="Email"><svg width="17" height="13" viewBox="0 0 17 13"><rect x="1" y="1" width="15" height="11" rx="1" fill="none" stroke="#5fc0f5" stroke-width="2"/><path d="M1 1l7.5 6L16 1" fill="none" stroke="#5fc0f5" stroke-width="2"/></svg></span>
      <span aria-label="Social link"></span>
      <span aria-label="Social link"></span>
      <span aria-label="Social link"></span>
    </div>
    <div class="copyright">© 2011 - Fetchora, All Rights Reserved</div>
  </footer>
</div>
</body>
</html>
```